Billboard design - consider what a billboard is

Design a billboard using my logo - Billboard is 6m x 3m
A Billboard is advertising for my company that is on a big sign.

Has to be clean and easy to read, and ideally highlights that we are Residential and Commercial builders.

Keep it clean and easy to read

The contact number for the board is

022 583 7092
www.harbourframeworks.co.nz
info@harbourframeworks.co.nz

Doesnt have to have all contact details if it doesnt fit

Has to catch peoples attention to contact us if they need a builder

Can you please change the sign to be all white writing, with black background ?
Updates

Please consider what a billboard is...

The design needs to be suitable for a billboard..

Target Market(s)

people driving past

Industry/Entity Type

Construction

Logo Text

Wellington Builder, website email address, contact number

Colors
0054AA
0677BA
7BADD7
CADEEF
E8F1F8

Requirements
Must have
• Easy to read
Nice to have
• easy to read, can clearly see contact details

```html
<!DOCTYPE html>
<html lang="en">
<head>
<meta charset="utf-8">
<title>Harbour Frameworks Billboard</title>
<link href="https://fonts.googleapis.com/css2?family=Archivo:wght@700&family=Arimo:wght@400&family=Roboto+Condensed:wght@700&display=swap" rel="stylesheet">
<style>
  :root {
    --page: #ffffff;
    --board: #1a1617;
    --blue: #5a8ac9;
    --stone: #6e6562;
    --white: #ffffff;
  }
  html, body {
    margin: 0;
    width: 1200px;
    height: 1200px;
    overflow: hidden;
    background: var(--page);
  }
  .canvas {
    position: relative;
    width: 1200px;
    height: 1200px;
  }
  .billboard {
    position: absolute;
    left: 150px;
    top: 376px;
    width: 899px;
    height: 449px;
    background: var(--board);
  }
  .frame-top {
    position: absolute;
    left: 20px;
    top: 17px;
    width: 857px;
    height: 312px;
    border: 3px solid var(--blue);
    border-bottom: none;
  }
  .frame-bottom {
    position: absolute;
    left: 20px;
    top: 384px;
    width: 857px;
    height: 45px;
    border: 3px solid var(--white);
    border-top: none;
  }
  .phone-tag {
    position: absolute;
    left: 309px;
    top: 81px;
    width: 397px;
    height: 37px;
    background: var(--stone);
    color: var(--white);
    font-family: "Roboto Condensed", sans-serif;
    font-weight: 700;
    font-size: 35px;
    line-height: 37px;
    display: flex;
    align-items: center;
    justify-content: center;
    gap: 12px;
  }
  .phone-tag svg { width: 32px; height: 26px; }
  .brand-mark {
    position: absolute;
    left: 190px;
    top: 175px;
    width: 100px;
    height: 100px;
    background: var(--stone);
  }
  .brand-name {
    position: absolute;
    left: 306px;
    top: 136px;
    margin: 0;
    color: var(--blue);
    font-family: "Archivo", sans-serif;
    font-weight: 700;
    font-size: 74px;
    line-height: 84px;
    letter-spacing: -1px;
  }
  .web-band {
    position: absolute;
    left: 0;
    top: 339px;
    width: 899px;
    height: 37px;
    background: var(--blue);
  }
  .contact-line {
    position: absolute;
    left: 0;
    width: 899px;
    display: flex;
    align-items: center;
    justify-content: center;
    gap: 10px;
    font-family: "Arimo", sans-serif;
    font-size: 29px;
  }
  .contact-web { top: 339px; height: 37px; color: var(--white); }
  .contact-email { top: 386px; height: 37px; color: var(--stone); }
  .contact-line svg { width: 24px; height: 24px; }
</style>
</head>
<body>
<div class="canvas">
  <div class="billboard">
    <div class="frame-top"></div>
    <div class="frame-bottom"></div>

    <div class="phone-tag">
      <svg viewBox="0 0 32 26" aria-hidden="true">
        <path d="M2 9 Q16 0 30 9 L27 13 L22 11 L22 8 Q16 6 10 8 L10 11 L5 13 Z" fill="#fff"/>
        <rect x="7" y="12" width="18" height="12" rx="2" fill="#fff"/>
        <g fill="#6e6562">
          <rect x="11" y="15" width="2" height="2"/><rect x="15" y="15" width="2" height="2"/><rect x="19" y="15" width="2" height="2"/>
          <rect x="11" y="19" width="2" height="2"/><rect x="15" y="19" width="2" height="2"/><rect x="19" y="19" width="2" height="2"/>
        </g>
      </svg>
      <span>022 583 7092</span>
    </div>

    <div class="brand-mark"></div>
    <h1 class="brand-name">Harbour<br>Frameworks</h1>

    <div class="web-band"></div>
    <div class="contact-line contact-web">
      <svg viewBox="0 0 24 24" aria-hidden="true" fill="none" stroke="#fff" stroke-width="1.6">
        <circle cx="12" cy="12" r="10"/>
        <ellipse cx="12" cy="12" rx="4.5" ry="10"/>
        <line x1="2" y1="12" x2="22" y2="12"/>
        <path d="M4 6.5 H20 M4 17.5 H20"/>
      </svg>
      <span>www.harbourframeworks.co.nz</span>
    </div>
    <div class="contact-line contact-email">
      <svg viewBox="0 0 24 24" aria-hidden="true">
        <rect x="1" y="5" width="22" height="15" fill="#6e6562"/>
        <path d="M1 5 L12 14 L23 5" fill="none" stroke="#1a1617" stroke-width="1.5"/>
      </svg>
      <span>info@harbourframeworks.co.nz</span>
    </div>
  </div>
</div>
</body>
</html>
```